Petal Sprite - web design for my new flower atelier

I would like to ask for design proposal for my newly established flower atelier. My brand name is Petal Sprite and I focus on realisation of events and flower projects (any kind) for physical as well as legel persons. I don’t operate as a standard flowershop. I would like to have 5 key parts - 1/Landing pg/welcome, 2/About me, 3/Gallery, 4/References, 5/Contact details. I would like the web design to reflect the way I am/ I do the things, ie, be slightly different, do non-tradiotional arrangements, my passion for flowers, gentle& fregile style, love for minimalism and details in the arrangements. I attach couple of photos of what I do so that you can better understand my style . You can see more on IG mirka_petal_sprite or FB Petal Sprite. I was wondering maybe one of the first 2 photos could be part of the landing pg. Or another idea is to have a design similar to this one https://thistlebloomstudio.example, ie to choose 3-5photos which are being animated like here. However, I am open to discuss any ideas and look forward for all the proposals.

Target Market(s)

physical as well as legal persons - weddings, celebrations, business events, projects for hotels, beaty salons, restaurants and others.. actually any kind of flower project

Industry/Entity Type

flowers

Number of Pages Required

1 page

Font styles to use
Other font styles liked:
• the font which matches the logo font style

Requirements
Must have
• to reflect the way I am as described above, I prefer more simple way of design, with the attention to a detail, I prefer pastel colours

```html
<!DOCTYPE html>
<html lang="en">
<head>
<meta charset="utf-8">
<title>Petal Sprite – Flower Atelier</title>
<link rel="stylesheet" href="https://fonts.googleapis.com/css2?family=Allura&family=Montserrat:wght@400;500;600&display=swap">
<style>
:root{
  --brown:#735b36;
  --brown-dark:#5e4a2b;
  --cream:#f5f0ea;
  --white:#ffffff;
  --ink:#3a3a3a;
  --text:#4a4a4a;
  --footer:#161616;
  --script:'Allura', cursive;
  --sans:'Montserrat', sans-serif;
}
*{box-sizing:border-box;margin:0;padding:0}
html,body{width:1200px;height:3029px;overflow:hidden;background:var(--white)}
body{position:relative;font-family:var(--sans);color:var(--text)}
.abs{position:absolute}
.caps{text-transform:uppercase;font-weight:600;letter-spacing:4px}

/* hero */
.hero{left:0;top:0;width:1200px;height:621px;
  background:linear-gradient(100deg,#c9bfae 0%,#8c7f6a 22%,#3a3129 45%,#241f1b 75%,#2e2a26 100%)}
.hero-shade{left:0;top:470px;width:1200px;height:151px;background:linear-gradient(180deg,rgba(0,0,0,0),rgba(200,200,195,.55))}
.hero-vase{left:170px;top:90px;width:330px;height:530px;border-radius:40% 40% 10% 10%;
  background:radial-gradient(ellipse at 50% 30%,#e8a050 0%,#c07a3a 25%,rgba(140,160,70,.8) 55%,rgba(170,190,90,.4) 80%,rgba(0,0,0,0) 100%)}
.logo-box{left:171px;top:0;width:113px;height:121px;background:var(--white);display:flex;align-items:center;justify-content:center;text-align:center}
.logo-box span{font-family:var(--sans);font-size:13px;font-weight:500;color:var(--brown);letter-spacing:2px;text-transform:uppercase;line-height:1.5}
.nav{top:34px;left:0;width:1200px;height:20px}
.nav a{position:absolute;top:0;color:var(--white);text-decoration:none;font-size:14px;font-weight:500;letter-spacing:3px;text-transform:uppercase}
.arrow{top:282px}
.hero-title{left:586px;top:196px;font-family:var(--script);font-size:96px;color:var(--white);line-height:1;white-space:nowrap}
.hero-text{left:579px;top:331px;width:400px;font-size:15px;line-height:23px;color:var(--white)}
.btn-light{left:579px;top:401px;width:147px;height:43px;background:var(--white);color:var(--brown);font-size:13px;display:flex;align-items:center;justify-content:center}

/* welcome */
.welcome-small{left:176px;top:800px;font-family:var(--script);font-size:36px;color:var(--brown);line-height:1}
.welcome-name{left:172px;top:838px;width:320px;font-family:var(--script);font-size:76px;color:var(--brown);line-height:1;white-space:nowrap}
.welcome-text{left:533px;top:694px;width:490px;font-size:16px;line-height:28.5px;color:var(--text)}
.btn-solid{left:534px;top:894px;width:145px;height:39px;background:var(--brown);color:var(--white);font-size:13px;display:flex;align-items:center;justify-content:center}

/* services */
.services{left:0;top:1029px;width:1200px;height:522px;background:var(--brown)}
.section-script{width:1200px;left:0;text-align:center;font-family:var(--script);line-height:1;font-weight:400}
.services-title{top:1050px;font-size:70px;color:var(--white)}
.services-sub{left:0;width:1200px;top:1125px;text-align:center;color:var(--white);font-size:15px;letter-spacing:5px}
.card-frame{width:186px;height:247px;border:1px solid rgba(255,255,255,.35)}
.card-photo{width:186px;height:247px}
.card-label{width:220px;text-align:center;color:var(--white);font-size:15px;letter-spacing:5px;line-height:21px}
.btn-outline{width:186px;height:33px;border:1px solid var(--white);color:var(--white);font-size:13px;display:flex;align-items:center;justify-content:center}

/* gallery */
.gallery-title{top:1606px;font-size:76px;color:var(--ink)}
.tile{width:193px;height:188px}
.tile-overlay{left:391px;top:1714px;width:193px;height:188px;background:rgba(115,91,54,.82);display:flex;align-items:center;justify-content:center;color:var(--white);font-size:15px;letter-spacing:5px}

/* contact */
.contact{left:0;top:2232px;width:1200px;height:455px;background:var(--brown)}
.contact-title{top:2280px;font-size:70px;color:var(--white)}
.field{background:var(--cream);color:#555;font-size:15px;padding:0 12px;display:flex;align-items:center}
.field.message{align-items:flex-start;padding-top:12px}
.btn-send{left:534px;top:2606px;width:132px;height:34px}

/* footer */
.footer{left:0;top:2687px;width:1200px;height:342px;background:var(--footer)}
.foot-head{color:var(--white);font-size:14px;letter-spacing:4px;text-align:center;width:300px}
.foot-line{color:var(--white);font-size:13.5px;text-align:center;width:300px}
.foot-logo{left:450px;top:2850px;width:300px;text-align:center;font-family:var(--sans);font-size:17px;font-weight:500;letter-spacing:3px;color:var(--brown);text-transform:uppercase}
.social{width:28px;height:28px;border:1px solid var(--brown);border-radius:50%}
</style>
</head>
<body>

<!-- hero -->
<div class="abs hero" role="img" aria-label="Photo of a green glass vase with orange and yellow flowers on a sunlit table"></div>
<div class="abs hero-vase" role="img" aria-label="Flower arrangement in a green cut-glass vase"></div>
<div class="abs hero-shade"></div>
<div class="abs logo-box"><span>Petal<br>Sprite</span></div>
<nav class="abs nav">
  <a style="left:381px">Home</a>
  <a style="left:487px">About me</a>
  <a style="left:636px">Gallery</a>
  <a style="left:769px">References</a>
  <a style="left:939px">Contact</a>
</nav>
<svg class="abs arrow" style="left:172px" width="38" height="72" viewBox="0 0 38 72"><polyline points="36,1 2,36 36,71" fill="none" stroke="#fff" stroke-width="1.3"/></svg>
<svg class="abs arrow" style="left:992px" width="38" height="72" viewBox="0 0 38 72"><polyline points="2,1 36,36 2,71" fill="none" stroke="#fff" stroke-width="1.3"/></svg>
<div class="abs hero-title">Petal Sprite</div>
<p class="abs hero-text">Donec interdum lacus nec pus fermentum, in lobortis magna aliquam. Proin congue iaculis augue.</p>
<div class="abs btn-light caps">Know more</div>

<!-- welcome -->
<div class="abs welcome-small">Welcome To</div>
<div class="abs welcome-name">Petal Sprite</div>
<p class="abs welcome-text">Quisque malesuada sagittis orci ut condimentum. Donec tortor risus, pretium at nunc vel, maximus euismod elit. Nulla quis eleif­end massa, id sagittis tellus. Vivamus suscipit nec erat id fermen­tum. Cras tortor mauris, scelerisque ac fringilla nec, aliquet ac ex. Quisque commodo mauris turpis, non lacinia neque consequat vitae. In facilisis finibus porta.</p>
<div class="abs btn-solid caps">Read more</div>

<!-- services -->
<section class="abs services"></section>
<h2 class="abs section-script services-title">How Can We Help</h2>
<div class="abs services-sub caps">Step by step process</div>

<div class="abs card-frame" style="left:240px;top:1163px"></div>
<div class="abs card-photo" style="left:235px;top:1168px;background:linear-gradient(160deg,#9a5a3a,#6e4a2e 50%,#c98a4a)" role="img" aria-label="Bird of paradise arrangement in front of a brick wall"></div>
<div class="abs card-label caps" style="left:218px;top:1424px">Weddings</div>
<div class="abs btn-outline caps" style="left:234px;top:1471px">Read more</div>

<div class="abs card-frame" style="left:513px;top:1163px"></div>
<div class="abs card-photo" style="left:508px;top:1168px;background:linear-gradient(160deg,#3d3226,#8a7a3a 45%,#d8c060 70%,#e8d8c8)" role="img" aria-label="Florist holding a yellow and peach bouquet"></div>
<div class="abs card-label caps" style="left:491px;top:1424px">Corporate<br>events</div>
<div class="abs btn-outline caps" style="left:507px;top:1471px">Read more</div>

<div class="abs card-frame" style="left:786px;top:1163px"></div>
<div class="abs card-photo" style="left:781px;top:1168px;background:linear-gradient(180deg,#6a3a24 0%,#9a6a4a 18%,#c06a3a 40%,#d8c8b8 62%,#f2f2f2 100%)" role="img" aria-label="Hanging suspended flower installation"></div>
<div class="abs card-label caps" style="left:764px;top:1424px">Rebloom</div>
<div class="abs btn-outline caps" style="left:780px;top:1471px">Read more</div>

<!-- gallery -->
<h2 class="abs section-script gallery-title">Our Gallery</h2>
<div class="abs tile" style="left:173px;top:1859px;background:radial-gradient(circle at 40% 40%,#e8eef0,#8a9a6a 55%,#4a5a2e)" role="img" aria-label="Daisies growing in a glass terrarium with moss"></div>
<div class="abs tile" style="left:391px;top:1714px;background:linear-gradient(160deg,#7a5a3a,#c8a060 60%,#a07040)" role="img" aria-label="Dried flower arrangement on a wooden table"></div>
<div class="abs tile-overlay caps">Flower 02</div>
<div class="abs tile" style="left:391px;top:1937px;background:linear-gradient(160deg,#a0583a,#c88a8a 45%,#6a7a5a 70%,#c8a070)" role="img" aria-label="Protea arrangement in a stone vase"></div>
<div class="abs tile" style="left:614px;top:1748px;background:linear-gradient(160deg,#7a4a30,#d88a6a 50%,#c89a5a)" role="img" aria-label="Coral tulips in a glass vase against brick"></div>
<div class="abs tile" style="left:614px;top:1969px;background:linear-gradient(100deg,#d0cfc8,#6a6a5a 50%,#3a3632)" role="img" aria-label="Orange and yellow flowers in a green glass vase"></div>
<div class="abs tile" style="left:835px;top:1859px;background:linear-gradient(160deg,#5a3a24,#d8a83a 50%,#c89050)" role="img" aria-label="Red flowers on a side table by yellow armchairs"></div>

<!-- contact -->
<section class="abs contact"></section>
<h2 class="abs section-script contact-title">Contact Us</h2>
<div class="abs field" style="left:216px;top:2371px;width:382px;height:43px">Name</div>
<div class="abs field" style="left:607px;top:2371px;width:381px;height:43px">Email</div>
<div class="abs field" style="left:216px;top:2425px;width:382px;height:45px">Phone</div>
<div class="abs field" style="left:607px;top:2425px;width:381px;height:45px">Subject</div>
<div class="abs field message" style="left:216px;top:2481px;width:772px;height:108px">Message</div>
<div class="abs btn-outline btn-send caps">Send now</div>

<!-- footer -->
<footer class="abs footer"></footer>
<div class="abs foot-head caps" style="left:163px;top:2745px">Contact info</div>
<svg class="abs" style="left:307px;top:2781px" width="12" height="14" viewBox="0 0 12 14"><path d="M6 0a5 5 0 0 0-5 5c0 4 5 9 5 9s5-5 5-9a5 5 0 0 0-5-5z" fill="#735b36"/><circle cx="6" cy="5" r="1.8" fill="#161616"/></svg>
<div class="abs foot-line" style="left:163px;top:2796px">48 Linden Row, Millbrook, MB 20417</div>
<svg class="abs" style="left:307px;top:2834px" width="13" height="10" viewBox="0 0 13 10"><rect width="13" height="10" fill="#735b36"/><polyline points="0,0 6.5,5.5 13,0" fill="none" stroke="#161616" stroke-width="1.2"/></svg>
<div class="abs foot-line" style="left:163px;top:2846px">hello@petalsprite.example</div>
<svg class="abs" style="left:307px;top:2882px" width="13" height="13" viewBox="0 0 24 24"><path d="M6.6 10.8a15 15 0 0 0 6.6 6.6l2.2-2.2a1 1 0 0 1 1-.25 11 11 0 0 0 3.6.6 1 1 0 0 1 1 1V20a1 1 0 0 1-1 1A17 17 0 0 1 3 4a1 1 0 0 1 1-1h3.5a1 1 0 0 1 1 1 11 11 0 0 0 .6 3.6 1 1 0 0 1-.25 1z" fill="#735b36"/></svg>
<div class="abs foot-line" style="left:163px;top:2896px">02 555 018 342</div>

<div class="abs foot-logo">Petal Sprite</div>
<div class="abs social" style="left:545px;top:2921px"></div>
<div class="abs social" style="left:586px;top:2921px"></div>
<div class="abs social" style="left:627px;top:2921px"></div>

<div class="abs foot-head caps" style="left:688px;top:2745px">Quick links</div>
<div class="abs foot-line" style="left:688px;top:2795px">Home</div>
<div class="abs foot-line" style="left:688px;top:2830px">About me</div>
<div class="abs foot-line" style="left:688px;top:2864px">Gallery</div>
<div class="abs foot-line" style="left:688px;top:2899px">References</div>
<div class="abs foot-line" style="left:688px;top:2933px">Contact</div>

</body>
</html>
```